Business Card for Beach theme sports bar called TAVRU

I need a business card designed for our employees, front and back. This will be used by the employees of two business locations to hand out to customers. I've attached the previous business cards we used at one time for a Benwicks (it is now Tavru). Looking for a fresh new card that is elegant but has character.

Target Market(s)

30-60, middle class

Contact Information for Business Card

We are a beach bar and sports bar. I am looking for an elegant business card with the front to have the TAVRU logo. Then on the back I need it to allow a space for employees to write their names and for them to write in their schedule. I have attached our old cards with our old name Benwicks so you can pull everything we need on the cards. one thing is missing is we have another location at 2815 N Willow Crest Rd with a number of 702-418-9351. Since we will use it for both locations it should allow the employee to circle or check mark the bar which they work at.

Font styles to use
Sans Serif

Requirements
Must have
• We are looking for some fresh ideas for the business card. Something that will really stick out to customers when the staff hands them out. Creativity will be looked at positively, but we still want it to look upscale and fun.

```html
<!DOCTYPE html>
<html lang="en">
<head>
<meta charset="utf-8">
<title>Tavru Business Card – Front and Back</title>
<link href="https://fonts.googleapis.com/css2?family=Bebas+Neue&family=Oswald:wght@400;500&display=swap" rel="stylesheet">
<style>
  :root {
    --page-bg: #2b2b2b;
    --card-red: #ee1c3a;
    --card-yellow: #f9ac1f;
    --maroon: #5a0303;
    --gold: #fbb829;
    --ink-red: #e8203a;
    --faint-mark: #d68c26;
  }
  * { margin: 0; padding: 0; box-sizing: border-box; }
  html, body {
    width: 1200px; height: 1000px; overflow: hidden;
    background: var(--page-bg);
  }
  .card { position: absolute; overflow: hidden; }

  /* Front */
  .card-front {
    left: 240px; top: 65px; width: 720px; height: 410px;
    background: var(--card-red);
  }
  .tagline {
    position: absolute; left: 32px; top: 62px;
    font: 30px/1 "Bebas Neue", sans-serif; color: var(--maroon);
  }
  .group-name {
    position: absolute; left: 32px; top: 91px;
    font: 400 13px/1 "Oswald", sans-serif; letter-spacing: 2.4px;
    color: var(--gold);
  }
  .brand-name {
    position: absolute; left: 50px; width: 440px; top: 125px;
    text-align: center;
    font: 190px/1 "Bebas Neue", sans-serif; color: var(--maroon);
    letter-spacing: 6px; white-space: nowrap;
  }
  .offer {
    position: absolute; right: 34px; top: 262px; width: 170px; text-align: center;
    font-family: "Bebas Neue", sans-serif; color: var(--gold);
  }
  .offer-amount { font-size: 92px; line-height: .9; display: block; }
  .offer-label { font-size: 40px; line-height: 1; display: block; }

  /* Back */
  .card-back {
    left: 236px; top: 522px; width: 728px; height: 415px;
    background: var(--card-yellow);
  }
  .watermark-name {
    position: absolute; left: 0; right: 0; top: 70px; text-align: center;
    font: 260px/1 "Bebas Neue", sans-serif; color: var(--faint-mark);
    opacity: .75; letter-spacing: 8px;
  }
  .rule { position: absolute; height: 2px; background: var(--maroon); }
  .schedule-days, .schedule-ticks {
    position: absolute; left: 70px; width: 250px;
    display: flex; justify-content: space-between;
    font: 500 16px/1 "Oswald", sans-serif; color: var(--ink-red);
  }
  .schedule-days { top: 58px; }
  .schedule-ticks { top: 100px; padding: 0 30px 0 24px; }
  .field-label {
    position: absolute; left: 462px; top: 52px;
    font: 34px/1 "Bebas Neue", sans-serif; color: var(--ink-red);
  }
  .location { position: absolute; top: 165px; text-align: center; }
  .location-left { left: 48px; width: 240px; }
  .location-right { left: 434px; width: 240px; }
  .check-box {
    display: block; margin: 0 auto 12px; width: 50px; height: 14px;
    border-left: 2px solid var(--maroon); border-right: 2px solid var(--maroon);
  }
  .address {
    font: 400 16px/1.4 "Oswald", sans-serif; color: var(--ink-red);
    text-transform: uppercase; white-space: nowrap;
  }
  .phone {
    margin-top: 8px;
    font: 400 36px/1 "Oswald", sans-serif; color: var(--maroon);
    transform: scaleX(.92); white-space: nowrap;
  }
  .fine-print {
    position: absolute; left: 70px; top: 332px;
    font: 400 13px/1.7 "Oswald", sans-serif; color: var(--ink-red);
    text-transform: uppercase; white-space: nowrap;
  }
  .contact-email {
    position: absolute; left: 70px; top: 376px;
    font: 400 12px/1 "Oswald", sans-serif; color: var(--maroon);
  }
</style>
</head>
<body>

<section class="card card-front" aria-label="Card front">
  <p class="tagline">A Gamers Bar</p>
  <p class="group-name">TAVRU TAVERN GROUP</p>
  <p class="brand-name">Tavru</p>
  <p class="offer">
    <span class="offer-amount">$20</span>
    <span class="offer-label">Match Play</span>
  </p>
</section>

<section class="card card-back" aria-label="Card back">
  <p class="watermark-name" aria-hidden="true">Tavru</p>

  <div class="schedule-days">
    <span>M</span><span>|</span><span>T</span><span>|</span><span>W</span><span>|</span><span>TH</span><span>|</span><span>F</span><span>|</span><span>SA</span><span>|</span><span>SU</span>
  </div>
  <div class="rule" style="left:70px; top:82px; width:250px;"></div>
  <div class="schedule-ticks"><span>|</span><span>|</span><span>|</span><span>|</span><span>|</span><span>|</span><span>|</span></div>
  <div class="rule" style="left:70px; top:132px; width:250px;"></div>

  <p class="field-label">Bartender</p>
  <div class="rule" style="left:407px; top:86px; width:250px;"></div>
  <div class="rule" style="left:407px; top:132px; width:250px;"></div>

  <div class="location location-left">
    <span class="check-box" aria-label="Check box"></span>
    <p class="address">3160 W Harlow Ridge Rd<br>Las Vegas, NV 89146</p>
    <p class="phone">702-530-6174</p>
  </div>
  <div class="location location-right">
    <span class="check-box" aria-label="Check box"></span>
    <p class="address">2815 N Willow Crest Rd<br>Las Vegas, NV 89146</p>
    <p class="phone">702-418-9351</p>
  </div>

  <div class="rule" style="left:70px; top:303px; width:587px;"></div>

  <p class="fine-print">Match play for new slot members. Must play total 100 coin. Please see bartender for details.<br>Management reserves all rights.</p>
  <p class="contact-email">CS@TAVRUBAR.COM</p>
</section>

</body>
</html>
```